Business Card Design for Engineering Firm

Need a business card design for small mechanical and plumbing engineering form based in Utah. Design should be customizable for all employees.

```html
<!DOCTYPE html>
<html lang="en">
<head>
<meta charset="utf-8">
<title>Harrowgate Engineering – Business Card</title>
<link rel="stylesheet" href="https://fonts.googleapis.com/css2?family=Open+Sans:wght@400;600&display=swap">
<style>
  :root {
    --bg: #e3e4e7;
    --paper: #ffffff;
    --brand-red: #8e1116;
    --brand-red-bright: #b3151c;
    --brand-red-deep: #5e0508;
    --panel-black: #141414;
    --panel-grey: #4a4a4a;
    --text-light: #ffffff;
    --shadow: rgba(0, 0, 0, 0.18);
  }
  * { box-sizing: border-box; margin: 0; padding: 0; }
  html, body {
    width: 1200px; height: 800px; overflow: hidden;
    background: var(--bg);
    font-family: "Open Sans", Arial, sans-serif;
  }
  .sheet {
    position: relative; width: 1200px; height: 800px;
    display: flex; align-items: center; justify-content: center; gap: 60px;
  }
  .card {
    position: relative; width: 525px; height: 300px; overflow: hidden;
    box-shadow: 0 10px 28px var(--shadow);
  }

  /* Back side */
  .card-back {
    background: radial-gradient(ellipse at 50% 45%, var(--brand-red-bright) 0%, var(--brand-red) 45%, var(--brand-red-deep) 100%);
    color: var(--text-light);
  }
  .card-back .brand-name {
    position: absolute; top: 92px; left: 0; right: 0;
    display: flex; align-items: center; justify-content: center; gap: 10px;
    font-size: 22px; font-weight: 600; letter-spacing: 2px;
  }
  .brand-square { width: 14px; height: 14px; background: currentColor; }
  .card-back .divider {
    position: absolute; top: 178px; left: 40px; right: 40px;
    height: 1px; background: rgba(255, 255, 255, 0.7);
  }
  .card-back .website {
    position: absolute; top: 150px; left: 0; right: 0; text-align: center;
    font-size: 14px; letter-spacing: 1.5px;
  }

  /* Front side */
  .card-front { background: var(--paper); }
  .card-front .panel { position: absolute; inset: 0; }
  .card-front .brand-name {
    position: absolute; top: 42px; left: 36px;
    display: flex; align-items: center; gap: 10px;
    color: var(--brand-red);
    font-size: 20px; font-weight: 600; letter-spacing: 1.5px; line-height: 1.2;
  }
  .contact {
    position: absolute; right: 26px; top: 98px;
    text-align: right; color: var(--text-light);
    font-size: 12px; line-height: 1.45;
  }
  .contact .person { color: var(--brand-red-bright); font-size: 14px; font-weight: 600; letter-spacing: 0.5px; }
  .contact .company { color: var(--brand-red-bright); margin-top: 6px; }
  .contact .lines { margin-top: 12px; }
  .contact-line { display: flex; justify-content: flex-end; align-items: center; gap: 8px; }
  .contact-line svg { width: 11px; height: 11px; flex: none; }
</style>
</head>
<body>
<main class="sheet">

  <section class="card card-back" aria-label="Business card back">
    <div class="brand-name"><span class="brand-square"></span>HARROWGATE ENGINEERING</div>
    <p class="website">www.harrowgateengineering.com</p>
    <div class="divider"></div>
  </section>

  <section class="card card-front" aria-label="Business card front">
    <svg class="panel" viewBox="0 0 525 300" aria-hidden="true">
      <polygon points="265,62 525,62 525,300 175,300 138,198" fill="var(--panel-grey)"/>
      <polygon points="290,82 525,82 525,300 205,300 168,202" fill="var(--panel-black)"/>
    </svg>

    <div class="brand-name"><span class="brand-square"></span><span>HARROWGATE<br>ENGINEERING</span></div>

    <div class="contact">
      <div class="person">DALE MERCER</div>
      <div>Director</div>
      <div class="company">Harrowgate Engineering</div>
      <div>99 dummy city</div>
      <div>dummy place 0000</div>
      <div class="lines">
        <div class="contact-line">300-555-0142
          <svg viewBox="0 0 12 12"><rect x="3" y="0.5" width="6" height="11" rx="1" fill="none" stroke="var(--brand-red-bright)" stroke-width="1.2"/><circle cx="6" cy="9.5" r="0.8" fill="var(--brand-red-bright)"/></svg>
        </div>
        <div class="contact-line">300-555-0142
          <svg viewBox="0 0 12 12"><path d="M2 1.5 L4.5 1 L5.5 3.8 L4 5 Q5 7.5 7 8 L8.2 6.5 L11 7.5 L10.5 10 Q5 11 2 1.5Z" fill="var(--brand-red-bright)"/></svg>
        </div>
        <div class="contact-line">info@harrowgateengineering.com
          <svg viewBox="0 0 12 12"><rect x="0.6" y="2.5" width="10.8" height="7.5" fill="none" stroke="var(--brand-red-bright)" stroke-width="1.2"/><path d="M0.6 2.5 L6 7 L11.4 2.5" fill="none" stroke="var(--brand-red-bright)" stroke-width="1.2"/></svg>
        </div>
        <div class="contact-line">www.harrowgateengineering.com
          <svg viewBox="0 0 12 12"><circle cx="6" cy="6" r="5" fill="none" stroke="var(--brand-red-bright)" stroke-width="1.2"/><ellipse cx="6" cy="6" rx="2.2" ry="5" fill="none" stroke="var(--brand-red-bright)" stroke-width="1"/><line x1="1" y1="6" x2="11" y2="6" stroke="var(--brand-red-bright)" stroke-width="1"/></svg>
        </div>
      </div>
    </div>
  </section>

</main>
</body>
</html>
```